American pesto sauce company needs a vintage/ old fashioned package design

Company name: Marisol Sauce.
We need a food label design for 4 different flavors of pesto sauce: classic almond, sundried tomato, roasted red pepper, and Cajun spice. For those that do not know what pesto is, it is a sauce like tomato sauce that is traditionally Italian and goes on pasta or whatever you choose to put it on and the consistent ingredients are garlic, cheese, nuts, olive oil and basil. They are fresh, all natural without preservatives, artificial flavors or colors.
The design of the jar is an old fashioned wire bale jar used for preserving foods ( attached is a picture). I'm looking for a label with:
• an upscale vintage feel but will also stand out on a grocery store shelf. I have attached an example of the feel I am looking for as well as the format of the words with my company name.
• The word "Pesto" must be prominent on the label.
• metalic gold boarders that go around the whole label maybe with gold embellishments if you see fit for that upscale feeling.
• Also, as you can see in the attachment, there are different typesets. And it must be easy to read from at least 3 feet away.
• Each label will have a different color corresponding to the flavor- could be part of the flavor text
• The bottom of the front panel must have “Net Wt. 5.75 oz (162g)” in a creative format how you see fit. Measures: height-28 mm, width-75mm
• Need logo for top part of label with the letters MS for Marisol Sauce and it will also contain the website, address and parent company name, use by date, etc. Measures:50 mm diameter
• The back panel of the label will contain the nutrition facts, ingredients and bar code. Measures: height-28 mm, width-75mm

Also the label is one piece with 3 different sections. Attached will be an example with measurements.
Updates

Check out this website on packaging. I absolutely love love love the Harwell Pantry almond water labels. The colors for the different flavors. How its not just horizontal or vertical. The different typesets/fonts/typography. The flourishes and background thats faded.
http://brightwrapgallery.com/page/3/

Target Market(s)

Target market is medium- high income foodies between 35-65

Industry/Entity Type

Grocery Store

Requirements
Must have
• Net Wt on front lower panel. Separation of the company name Marisol & Pesto. See attachment.
Nice to have
• Name of flavor designed in a wave pattern as shown in attachment. Hand drawn font OK.

```html
<!DOCTYPE html>
<html lang="en">
<head>
<meta charset="utf-8">
<title>Marisol Sauce — Classic Almond Pesto Label</title>
<link rel="stylesheet" href="https://fonts.googleapis.com/css2?family=Lobster&family=Old+Standard+TT:wght@400;700&family=Archivo:wght@500&display=swap">
<style>
  :root {
    --backdrop: #efeeec;
    --paper: #f2ece1;
    --paper-edge: #e2d9c8;
    --maroon: #5b1f20;
    --wine: #7a2427;
    --ink: #4a3430;
    --almond: #b27a4e;
  }
  html, body {
    margin: 0;
    width: 1200px;
    height: 1190px;
    overflow: hidden;
    background: var(--backdrop);
  }
  .label-sheet { display: block; width: 1200px; height: 1190px; }
  .paper { fill: var(--paper); stroke: var(--paper-edge); stroke-width: 1; }
  .dotted-frame { fill: none; stroke: var(--wine); stroke-width: 1.4; stroke-dasharray: 1.5 3; }
  .brand-seal { fill: var(--maroon); }
  .seal-ring { fill: none; stroke: var(--paper); stroke-width: 1; opacity: .6; }
  .brand-name { font-family: "Old Standard TT", serif; font-size: 19px; fill: var(--paper); letter-spacing: 2px; }
  .ring-text { font-family: "Archivo", sans-serif; font-size: 11.5px; fill: var(--ink); letter-spacing: 1.2px; }
  .size-note { font-family: "Old Standard TT", serif; font-size: 11px; fill: var(--wine); font-style: italic; }
  .product-word { font-family: "Old Standard TT", serif; font-weight: 700; font-size: 24px; fill: var(--wine); letter-spacing: 1px; }
  .flavor-name { font-family: "Lobster", cursive; font-size: 42px; fill: var(--wine); }
  .tagline { font-family: "Archivo", sans-serif; font-size: 9.5px; fill: var(--ink); letter-spacing: .8px; }
  .weight { font-family: "Archivo", sans-serif; font-size: 9px; fill: var(--ink); }
  .rule { stroke: var(--wine); stroke-width: 1; }
  .strip-rule { stroke: var(--wine); stroke-width: .8; opacity: .5; }
</style>
</head>
<body>
<svg class="label-sheet" viewBox="0 0 1200 1190" xmlns="http://www.w3.org/2000/svg">
  <defs>
    <linearGradient id="strip-fade" x1="0" y1="0" x2="0" y2="1">
      <stop offset="0" stop-color="#f2ece1" stop-opacity="0"/>
      <stop offset=".12" stop-color="#f2ece1" stop-opacity="1"/>
    </linearGradient>
    <path id="ring-path" d="M600,392 m-84,0 a84,84 0 1,1 168,0 a84,84 0 1,1 -168,0"/>
  </defs>

  <!-- neck strip -->
  <g class="neck-strip">
    <rect x="567" y="200" width="66" height="570" fill="url(#strip-fade)"/>
    <line class="strip-rule" x1="600" y1="215" x2="600" y2="270"/>
    <line class="strip-rule" x1="600" y1="540" x2="600" y2="720"/>
  </g>

  <!-- top seal -->
  <g class="top-seal">
    <g class="paper">
      <circle cx="600" cy="392" r="100"/>
      <circle cx="600" cy="290" r="16"/><circle cx="651" cy="304" r="16"/>
      <circle cx="688" cy="341" r="16"/><circle cx="702" cy="392" r="16"/>
      <circle cx="688" cy="443" r="16"/><circle cx="651" cy="480" r="16"/>
      <circle cx="600" cy="494" r="16"/><circle cx="549" cy="480" r="16"/>
      <circle cx="512" cy="443" r="16"/><circle cx="498" cy="392" r="16"/>
      <circle cx="512" cy="341" r="16"/><circle cx="549" cy="304" r="16"/>
    </g>
    <circle cx="600" cy="392" r="100" fill="var(--paper)"/>
    <text class="ring-text">
      <textPath href="#ring-path" startOffset="2%">2180 Alder Ave, Brookfield, NY</textPath>
    </text>
    <text class="ring-text">
      <textPath href="#ring-path" startOffset="54%">Corvel Fine Foods, LLC •</textPath>
    </text>
    <circle class="brand-seal" cx="600" cy="392" r="62"/>
    <circle class="seal-ring" cx="600" cy="392" r="56"/>
    <text class="brand-name" x="600" y="388" text-anchor="middle">Marisol</text>
    <text class="brand-name" x="600" y="412" text-anchor="middle">Sauce</text>
  </g>

  <!-- front panel -->
  <g class="front-panel">
    <path class="paper" d="M442,758 H768 A14,14 0 0,0 782,772 V868 A14,14 0 0,0 768,882 H442 A14,14 0 0,0 428,868 V772 A14,14 0 0,0 442,758 Z"/>
    <path class="dotted-frame" d="M450,766 H760 A10,10 0 0,0 774,778 V862 A10,10 0 0,0 760,874 H450 A10,10 0 0,0 436,862 V778 A10,10 0 0,0 450,766 Z"/>
    <text class="size-note" x="508" y="782">4oz</text>
    <text class="product-word" x="530" y="784">PESTO</text>
    <text class="flavor-name" x="602" y="829" text-anchor="middle">Classic Almond</text>
    <line class="rule" x1="506" y1="840" x2="568" y2="840"/>
    <line class="rule" x1="634" y1="840" x2="712" y2="840"/>
    <line class="rule" x1="506" y1="849" x2="568" y2="849"/>
    <line class="rule" x1="634" y1="849" x2="712" y2="849"/>
    <text class="tagline" x="508" y="847">MOST</text>
    <text class="tagline" x="652" y="847">DELICIOUS</text>
    <text class="weight" x="515" y="860">162g</text>
    <text class="weight" x="652" y="860">Net Wt.</text>
    <text class="weight" x="652" y="870">5.75 oz</text>
    <ellipse role="img" aria-label="Illustration of two almonds" cx="604" cy="856" rx="38" ry="17" fill="var(--almond)"/>
  </g>
</svg>
</body>
</html>
```